Wendy Marsh Copywriter Website

I am starting a new business as a freelance copywriter. Trying to set up the website for my business is proving to be too technical for me. I would like a simple, clean website using primarily black and white. I have attached the logo I would like used. I would like the menu icons to be Home, Services, Portfolio, Blog, Contact. I would like my mobile phone number (0412 583 906) and email address (wendy.marsh.copywriter@mailbox-example.com) used in the header of the site. I need the site to be easily manageable and inter-changeable for me to be able to move things around and add images, etc with ease.

I would like the home page to be a static page with space for an image of myself somewhere (I haven't had this taken as yet), an area to put a bit about myself and my business, and also somewhere to include social media icons/links. Again, I would like the whole website and home page to be easily managed so that I can add/delete things with ease.

I would like the image of the typewriter used in the website somewhere also please.

Font styles to use
Sans Serif
Script

Colors
fdf0f6

Requirements
Must have
• The logo provided
• Ability to change page contents easily
• Ability to add social media icons as needed
Nice to have
• Use of the typewriter image
Should not have
• Complicated pages that are not easily editable

```html
<!DOCTYPE html>
<html lang="en">
<head>
<meta charset="utf-8">
<title>Wendy Marsh Copywriter</title>
<link rel="stylesheet" href="https://fonts.googleapis.com/css2?family=Dancing+Script:wght@500&family=Josefin+Sans:wght@300;400;600&family=Poppins:wght@500;600&display=swap">
<style>
:root{
  --ink:#000;
  --paper:#fff;
  --mist:#f6f6f6;
  --blush:#fdf0f6;
  --graphite:#555;
  --text:#333;
  --rule:#444;
  --script:"Dancing Script",cursive;
  --body:"Josefin Sans",sans-serif;
  --ui:"Poppins",sans-serif;
}
*{box-sizing:border-box;margin:0;padding:0}
html,body{width:1200px;height:3285px;overflow:hidden}
body{position:relative;background:var(--paper);font-family:var(--body);color:var(--text)}
.abs{position:absolute}
.script-title{font-family:var(--script);font-weight:500;color:var(--ink);font-size:40px;line-height:1}
.copy{font-size:15px;line-height:29px;font-weight:300;color:var(--text)}
.btn{display:flex;align-items:center;justify-content:center;background:var(--ink);color:var(--paper);font-family:var(--ui);font-weight:600;font-size:16px;border-radius:4px}

/* hero */
.hero{left:0;top:0;width:1200px;height:624px;background:#f3f3f3;overflow:hidden}
.brand{left:79px;top:32px;display:flex;align-items:center;gap:12px}
.brand-mark{width:26px;height:26px;background:var(--blush);border:1px solid #e9cbd8}
.brand-name{font-family:var(--body);font-weight:600;font-size:22px;color:var(--ink)}
.nav{left:477px;top:42px;font-family:var(--ui);font-weight:500;font-size:15px}
.nav span{position:absolute;white-space:nowrap;color:var(--paper)}
.nav .on-light{color:var(--ink)}
.search{left:1080px;top:32px;width:42px;height:42px;border-radius:50%;background:var(--paper)}
.hero-card{left:153px;top:116px;width:894px;height:416px;background:var(--paper);border-radius:6px;box-shadow:0 18px 30px rgba(0,0,0,.35);overflow:hidden}
.hero-photo{left:0;top:0;width:515px;height:416px;background:radial-gradient(circle at 35% 35%,#5a4a3e 0%,#261d17 35%,#0b0908 75%);clip-path:polygon(0 0,515px 0,449px 416px,0 416px)}
.socials-sq{left:744px;top:30px;display:flex;gap:6px}
.socials-sq i{display:block;width:22px;height:22px;background:var(--ink);border-radius:2px}
.hero-title{left:508px;top:108px;font-size:44px;white-space:nowrap}
.hero-copy{left:510px;top:190px;width:330px}
.hero-btn{left:508px;top:278px;width:145px;height:51px}

/* about */
.about-title{left:81px;top:694px}
.about-copy{left:81px;top:766px;width:690px;font-size:14.5px}
.about-btn{left:79px;top:970px;width:142px;height:51px}
.about-photo{left:854px;top:690px;width:219px;height:394px;background:linear-gradient(180deg,#ddd 0%,#9fc0de 45%,#86aad0 75%,#222 100%);border-radius:90px 90px 0 0}

/* services */
.services{left:0;top:1084px;width:1200px;height:488px;background:var(--mist)}
.services-art{left:77px;top:1143px;width:273px;height:368px;background:linear-gradient(180deg,#f2f2f2 0%,#e6e6e6 28%,#2b2b2b 45%,#111 100%);border-radius:6px}
.services-title{left:453px;top:1152px}
.services-copy{left:453px;top:1218px;width:610px;font-size:14.5px}
.svc{position:absolute;display:flex;gap:24px}
.svc-icon{width:61px;height:61px;background:var(--ink);border-radius:6px;flex:none;display:flex;align-items:center;justify-content:center}
.svc h3{font-family:var(--ui);font-weight:600;font-size:17px;color:var(--ink);margin:2px 0 6px;white-space:nowrap}
.svc p{font-size:14.5px;line-height:29px;font-weight:300;width:240px}

/* portfolio */
.section-title-c{left:0;width:1200px;text-align:center}
.tile{position:absolute;width:322px;height:206px;border-radius:3px}

/* blog */
.blog{left:0;top:2218px;width:1200px;height:460px;background:var(--mist)}
.blog-card{position:absolute;border-radius:2px}
.blog-overlay{left:0;bottom:0;width:324px;height:106px;background:rgba(40,40,40,.9);color:var(--paper);padding:14px 14px 0 14px}
.blog-overlay h4{font-family:var(--ui);font-weight:600;font-size:15px;line-height:25px}
.blog-meta{display:flex;gap:20px;margin-top:12px;font-size:12px;align-items:center}
.blog-meta span{display:flex;gap:6px;align-items:center}

/* newsletter */
.news-sub{top:2828px;font-size:14.5px;font-weight:300}
.field{position:absolute;top:2890px;width:322px;height:38px;border-bottom:1px solid var(--graphite);font-size:14.5px;font-weight:300;padding-top:8px}
.news-btn{left:869px;top:2878px;width:147px;height:50px}

/* footer */
.footer{left:0;top:2990px;width:1200px;height:295px;background:var(--ink);color:var(--paper)}
.contact{position:absolute;top:56px;width:420px;text-align:center}
.contact .ring{width:44px;height:44px;border-radius:50%;background:var(--paper);margin:0 auto 16px;display:flex;align-items:center;justify-content:center}
.contact h5{font-family:var(--ui);font-weight:600;font-size:17px}
.contact p{font-size:14px;margin-top:8px;white-space:nowrap}
.footer-rule{left:79px;top:220px;width:1042px;height:1px;background:var(--rule)}
.copyright{left:79px;top:250px;font-size:14px;letter-spacing:.5px}
.socials-c{left:925px;top:237px;display:flex;gap:12px}
.socials-c i{display:block;width:41px;height:41px;border-radius:50%;background:var(--paper)}
</style>
</head>
<body>

<section class="abs hero">
  <svg class="abs" style="left:0;top:0" width="1200" height="624" viewBox="0 0 1200 624" aria-hidden="true">
    <polygon points="657,0 1200,0 1200,624 570,624" fill="#000"/>
    <path d="M570,624 L620,430 C760,470 900,560 1200,470 L1200,624 Z" fill="#5c5c5c"/>
    <path d="M1200,360 C1100,400 1060,470 1200,520 Z" fill="#2c2c2c"/>
  </svg>
  <div class="abs brand"><i class="brand-mark"></i><span class="brand-name">Wendy Marsh Copywriter</span></div>
  <nav class="abs nav">
    <span class="on-light" style="left:0">Home</span>
    <span class="on-light" style="left:99px">Services</span>
    <span style="left:213px">Portfolio</span>
    <span style="left:331px">Blog</span>
    <span style="left:410px">Contact</span>
  </nav>
  <div class="abs search">
    <svg width="42" height="42" viewBox="0 0 42 42" aria-hidden="true"><circle cx="19" cy="19" r="6.5" fill="none" stroke="#000" stroke-width="3"/><line x1="24" y1="24" x2="29" y2="29" stroke="#000" stroke-width="3.5" stroke-linecap="round"/></svg>
  </div>
  <div class="abs hero-card">
    <div class="abs hero-photo" role="img" aria-label="Portrait of the copywriter at a typewriter in a dark, warmly lit room"></div>
    <div class="abs socials-sq"><i></i><i></i><i></i><i></i></div>
    <h1 class="abs script-title hero-title">Hi, I'm Wendy Marsh</h1>
    <p class="abs copy hero-copy">Lorem Ipsum is simply dummy text of the printing and typesetting the 1500s.</p>
    <a class="abs btn hero-btn">Contact Me</a>
  </div>
</section>

<h2 class="abs script-title about-title">About Wendy Marsh</h2>
<div class="abs copy about-copy">
  <p>Lorem Ipsum is simply dummy text of the printing and typesetting industry. Lorem Ipsum has been the industry's standard dummy text ever since the 1500s, when an unknown printer took a galley of type and scrambled it to make a type specimen book.</p>
  <p style="margin-top:28px">It has survived not only five centuries, but also the leap into electronic typesetting, remaining essentially unchanged. It was popularised in including versions of Lorem Ipsum.</p>
</div>
<a class="abs btn about-btn">Read More</a>
<div class="abs about-photo" role="img" aria-label="Photo of the copywriter in a light blue blouse with arms crossed"></div>

<section class="abs services"></section>
<div class="abs services-art" role="img" aria-label="Vintage black typewriter with a sheet of paper"></div>
<h2 class="abs script-title services-title">Services</h2>
<p class="abs copy services-copy">Lorem Ipsum is simply dummy text of the printing and typesetting industry. Lorem Ipsum has been the industry's standard dummy text ever since the 1500s,</p>

<div class="svc" style="left:449px;top:1314px">
  <div class="svc-icon"><svg width="30" height="30" viewBox="0 0 30 30" aria-hidden="true"><rect x="6" y="4" width="18" height="22" fill="none" stroke="#fff" stroke-width="2"/><path d="M20 8 L12 20 L11 23 L14 21 L22 10 Z" fill="#fff"/></svg></div>
  <div><h3>Blogging</h3><p>Lorem Ipsum is simply dummy text typesetting industry.</p></div>
</div>
<div class="svc" style="left:804px;top:1314px">
  <div class="svc-icon"><svg width="32" height="32" viewBox="0 0 32 32" aria-hidden="true"><g fill="none" stroke="#fff" stroke-width="1.8"><circle cx="16" cy="16" r="3.5"/><circle cx="6" cy="7" r="2.5"/><circle cx="26" cy="7" r="2.5"/><circle cx="6" cy="25" r="2.5"/><circle cx="26" cy="25" r="2.5"/><path d="M8 9 L13 14 M24 9 L19 14 M8 23 L13 18 M24 23 L19 18"/></g></svg></div>
  <div><h3>Social Copywriting</h3><p>Lorem Ipsum is simply dummy text typesetting industry.</p></div>
</div>
<div class="svc" style="left:449px;top:1428px">
  <div class="svc-icon"><svg width="30" height="30" viewBox="0 0 30 30" aria-hidden="true"><rect x="6" y="4" width="18" height="22" fill="none" stroke="#fff" stroke-width="2"/><rect x="9" y="8" width="6" height="5" fill="#fff"/><path d="M17 9h4M17 12h4M9 16h12M9 19h12M9 22h9" stroke="#fff" stroke-width="1.6"/></svg></div>
  <div><h3>SEO Articles</h3><p>Lorem Ipsum is simply dummy text typesetting industry.</p></div>
</div>
<div class="svc" style="left:804px;top:1428px">
  <div class="svc-icon"><svg width="30" height="30" viewBox="0 0 30 30" aria-hidden="true"><path d="M7 4h12l5 5v17H7Z" fill="none" stroke="#fff" stroke-width="2"/><path d="M10 12h10M10 16h10M10 20h7" stroke="#fff" stroke-width="1.6"/></svg></div>
  <div><h3>Press Release Writing</h3><p>Lorem Ipsum is simply dummy text typesetting industry.</p></div>
</div>

<h2 class="abs script-title section-title-c" style="top:1642px">Portfolio</h2>
<div class="tile" style="left:98px;top:1721px;background:linear-gradient(160deg,#f4f4f4,#d9d9d9 55%,#b9a08a)" role="img" aria-label="Hands typing on a vintage typewriter on a white desk"></div>
<div class="tile" style="left:438px;top:1721px;background:linear-gradient(160deg,#cfcfcf,#8c8c8c 60%,#4a4a4a)" role="img" aria-label="Woman writing at a typewriter against a grey wall"></div>
<div class="tile" style="left:779px;top:1721px;background:linear-gradient(160deg,#8a7f76,#d9d6d2 50%,#6f655c)" role="img" aria-label="Notebooks, phone and glasses on a wooden table"></div>
<div class="tile" style="left:98px;top:1947px;background:linear-gradient(160deg,#cfdbe4,#9fb6c6 55%,#6f8aa0)" role="img" aria-label="Black glasses resting on printed pages"></div>
<div class="tile" style="left:438px;top:1947px;background:linear-gradient(180deg,#ededed,#d3d3d3 45%,#2a2a2a 75%,#e4e4e4)" role="img" aria-label="Vintage typewriter on a white background"></div>
<div class="tile" style="left:779px;top:1947px;background:linear-gradient(160deg,#3a3a3a,#cfcfcf 45%,#f2f2f2)" role="img" aria-label="Laptop, open notebook, glasses and pen"></div>

<section class="abs blog"></section>
<h2 class="abs script-title section-title-c" style="top:2288px">Latest Blog</h2>
<div class="blog-card" style="left:77px;top:2387px;width:324px;height:208px;background:linear-gradient(150deg,#5c5c5c,#cfcfcf 35%,#a07c5b 70%,#e6e0da)" role="img" aria-label="Laptop and paper on a wooden desk"></div>
<div class="blog-card" style="left:438px;top:2365px;width:324px;height:250px;background:linear-gradient(180deg,#e4e4e4,#bdbdbd 35%,#2c2c2c 70%)" role="img" aria-label="Typewriter on a desk with a coffee cup">
  <svg class="abs" style="left:124px;top:52px" width="80" height="30" viewBox="0 0 80 30" aria-hidden="true"><circle cx="18" cy="14" r="7" fill="none" stroke="#fff" stroke-width="2.5"/><line x1="23" y1="19" x2="28" y2="24" stroke="#fff" stroke-width="2.5"/><g fill="#fff"><circle cx="62" cy="8" r="3.5"/><circle cx="52" cy="15" r="3.5"/><circle cx="62" cy="22" r="3.5"/></g><path d="M62 8L52 15L62 22" stroke="#fff" stroke-width="1.5" fill="none"/></svg>
  <div class="abs blog-overlay">
    <h4>Ragtime Returns to<br>Riverside Swing Festival 2017</h4>
    <div class="blog-meta">
      <span><svg width="14" height="12" viewBox="0 0 14 12" aria-hidden="true"><path d="M7 12L1 6A3 3 0 0 1 7 2A3 3 0 0 1 13 6Z" fill="#fff"/></svg>Likes</span>
      <span><svg width="16" height="12" viewBox="0 0 16 12" aria-hidden="true"><ellipse cx="8" cy="5" rx="7" ry="4.5" fill="none" stroke="#fff" stroke-width="1.6"/><path d="M3 8L2 12L6 9" fill="#fff"/></svg>Comments</span>
      <span><svg width="12" height="12" viewBox="0 0 12 12" aria-hidden="true"><rect x="1" y="2" width="10" height="9" fill="none" stroke="#fff" stroke-width="1.5"/><path d="M1 5h10" stroke="#fff" stroke-width="1.5"/></svg>15 July,2017</span>
    </div>
  </div>
</div>
<div class="blog-card" style="left:799px;top:2387px;width:324px;height:208px;background:linear-gradient(160deg,#8a7f76,#d9d6d2 50%,#6f655c)" role="img" aria-label="Notebooks and glasses on a wooden table"></div>

<h2 class="abs script-title section-title-c" style="top:2748px">Newsletter Subscription</h2>
<p class="abs section-title-c news-sub">For latest news or updates subscribe our newsletter</p>
<div class="field" style="left:184px">Name*</div>
<div class="field" style="left:528px">E-mail*</div>
<a class="abs btn news-btn">Subscribe</a>

<footer class="abs footer">
  <div class="contact" style="left:30px">
    <div class="ring"><svg width="22" height="22" viewBox="0 0 22 22" aria-hidden="true"><path d="M5 2l4 4-2 3c1 2 3 4 5 5l3-2 4 4-3 3C9 19 3 13 2 5Z" fill="#000"/></svg></div>
    <h5>Phone</h5><p>0412 583 906</p>
  </div>
  <div class="contact" style="left:389px">
    <div class="ring"><svg width="22" height="22" viewBox="0 0 22 22" aria-hidden="true"><rect x="2" y="5" width="18" height="12" fill="#000"/><path d="M2 5l9 7 9-7" stroke="#fff" stroke-width="1.5" fill="none"/></svg></div>
    <h5>E-mail</h5><p>wendy.marsh.copywriter@mailbox-example.com</p>
  </div>
  <div class="contact" style="left:750px">
    <div class="ring"><svg width="22" height="22" viewBox="0 0 22 22" aria-hidden="true"><rect x="6" y="2" width="10" height="6" fill="none" stroke="#000" stroke-width="1.8"/><rect x="2" y="8" width="18" height="9" rx="2" fill="#000"/><rect x="6" y="14" width="10" height="6" fill="#fff" stroke="#000" stroke-width="1.8"/></svg></div>
    <h5>Fax</h5><p>123 456 7890</p>
  </div>
  <div class="abs footer-rule"></div>
  <p class="abs copyright">© WENDY MARSH - 2018. All Rights Reserved.</p>
  <div class="abs socials-c"><i></i><i></i><i></i><i></i></div>
</footer>

</body>
</html>
```